Computer Support Rackcard

My company provides computer support services. Website is below:

www.nortekpcfix.com

The new service we are offering is Monthly Remote Support Service. I am trying to promote the service on a rackcard which I will give out to anyone who walks into my computer store. I want the design to be easy to read.

Our Remote Support service is available for $19.99 per pc and provides unlimited online computer support along with some extras such as antivirus and web filter to prevent computer viruses/malware. We would like to see designs that use royal blue color scheme and has a modern style like Vexel uses and is clean and easy to read.

I would like to somehow make the design look entertaining and would be interesting design wise. I hate templates so I want something that is not just a template with a picture and text added to it. Trying to be different with this design.
Updates

I uploaded a PSD file for my logo.

Target Market(s)

Target Customers are consumers with families with kids. Who are anywhere from age 40 to 65

Industry/Entity Type

Computer

Font styles to use
Serif
Sans Serif

Colors
0255a3
3176b5
85abd2
33a6d7
85cae6

Requirements
Must have
• Only 1 side of the rackcard needs to be designed.
Should not have
• The design should not have any pictures of people who appear to not be from United States. I don't want people to think my services are outsourced since they are not.

```html
<!DOCTYPE html>
<html lang="en">
<head>
<meta charset="utf-8">
<title>Halvern PC Care – Monthly Remote Support Service</title>
<link rel="stylesheet" href="https://fonts.googleapis.com/css2?family=Open+Sans:wght@400;600;700&display=swap">
<style>
  :root {
    --royal: #0255a3;
    --mid-blue: #3176b5;
    --soft-blue: #85abd2;
    --sky: #33a6d7;
    --pale-sky: #85cae6;
    --white: #ffffff;
    --ink: #1f2326;
  }
  * { margin: 0; padding: 0; box-sizing: border-box; }
  html, body { width: 1200px; height: 2700px; overflow: hidden; background: var(--white); }
  .rackcard {
    position: relative;
    width: 1200px;
    height: 2700px;
    font-family: "Open Sans", sans-serif;
    background: var(--white);
    overflow: hidden;
  }
  .hero {
    position: absolute;
    left: 0; top: 0;
    width: 1200px; height: 1244px;
    background: var(--mid-blue);
  }
  .brand-tab {
    position: absolute;
    left: 80px; top: -40px;
    width: 1040px; height: 222px;
    background: var(--white);
    border-radius: 0 0 50% 50% / 0 0 100% 100%;
    display: flex;
    align-items: center;
    justify-content: center;
    gap: 24px;
    padding-top: 30px;
  }
  .brand-mark {
    width: 40px; height: 40px;
    background: var(--royal);
  }
  .brand-name {
    font-weight: 700;
    font-size: 62px;
    letter-spacing: 3px;
    color: var(--royal);
    line-height: 1;
  }
  .price {
    position: absolute;
    left: 0; top: 340px;
    width: 1200px;
    text-align: center;
    color: var(--white);
    line-height: 1;
  }
  .price-amount { font-size: 214px; font-weight: 400; letter-spacing: 2px; }
  .price-unit { font-size: 42px; font-weight: 400; margin-left: 10px; }
  .service-title {
    position: absolute;
    left: 0; top: 644px;
    width: 1200px;
    text-align: center;
    color: var(--pale-sky);
    font-size: 130px;
    font-weight: 400;
    line-height: 176px;
  }
  .service-list {
    position: absolute;
    left: 0; top: 1244px;
    width: 1200px; height: 1244px;
    list-style: none;
  }
  .service-item {
    position: absolute;
    display: flex;
    align-items: center;
    gap: 80px;
    font-size: 72px;
    color: var(--ink);
    line-height: 1;
  }
  .service-icon { width: 96px; height: 96px; flex: none; }
  .contact-band {
    position: absolute;
    left: 0; top: 2488px;
    width: 1200px; height: 212px;
    background: var(--mid-blue);
    display: flex;
    align-items: center;
    justify-content: center;
    color: var(--pale-sky);
    font-size: 112px;
    letter-spacing: 2px;
    line-height: 1;
  }
</style>
</head>
<body>
<main class="rackcard">
  <section class="hero">
    <header class="brand-tab">
      <span class="brand-mark"></span>
      <span class="brand-name">HALVERN PC CARE</span>
    </header>
    <p class="price"><span class="price-amount">$19,99</span><span class="price-unit">/ Per PC</span></p>
    <h1 class="service-title">Monthly<br>Remote Support<br>Service</h1>
  </section>

  <ul class="service-list">
    <li class="service-item" style="left:48px; top:96px;">
      <svg class="service-icon" viewBox="0 0 24 24">
        <ellipse cx="10" cy="5" rx="8" ry="3" fill="var(--sky)"/>
        <path d="M2 5v5c0 1.7 3.6 3 8 3s8-1.3 8-3V5c0 1.7-3.6 3-8 3S2 6.7 2 5z" fill="var(--soft-blue)"/>
        <path d="M2 11v5c0 1.7 3.6 3 8 3 1 0 2-.1 3-.2V13c-1 .1-2 .2-3 .2-4.4 0-8-1.3-8-2.2z" fill="var(--sky)"/>
        <path d="M18 14v3h3v2h-3v3h-2v-3h-3v-2h3v-3z" fill="var(--sky)"/>
      </svg>
      <span>Data Recovery</span>
    </li>
    <li class="service-item" style="left:152px; top:248px;">
      <svg class="service-icon" viewBox="0 0 24 24">
        <path d="M12 2l8 3v6c0 5-3.4 9.3-8 11-4.6-1.7-8-6-8-11V5z" fill="var(--sky)"/>
        <path d="M8 12l3 3 5-6" stroke="var(--white)" stroke-width="2" fill="none" stroke-linecap="round"/>
      </svg>
      <span>Virus Removal</span>
    </li>
    <li class="service-item" style="left:200px; top:416px;">
      <svg class="service-icon" viewBox="0 0 24 24">
        <path d="M3 21l8-8" stroke="var(--sky)" stroke-width="2.5" stroke-linecap="round"/>
        <path d="M14 3a5 5 0 0 0-2 6l-2 2 3 3 2-2a5 5 0 0 0 6-2l-3 0-2-2 0-3z" fill="var(--sky)"/>
      </svg>
      <span>Troubleshotoing</span>
    </li>
    <li class="service-item" style="left:232px; top:568px;">
      <svg class="service-icon" viewBox="0 0 24 24">
        <circle cx="12" cy="12" r="6" fill="none" stroke="var(--sky)" stroke-width="3" stroke-dasharray="3 1.7"/>
        <circle cx="12" cy="12" r="3" fill="none" stroke="var(--sky)" stroke-width="2"/>
        <path d="M3 20h18" stroke="var(--soft-blue)" stroke-width="2"/>
      </svg>
      <span>New Program Install</span>
    </li>
    <li class="service-item" style="left:200px; top:728px;">
      <svg class="service-icon" viewBox="0 0 24 24">
        <path d="M3 4h16l-6 7v7l-4 2v-9z" fill="var(--sky)"/>
        <path d="M16 16l5 5M21 16l-5 5" stroke="var(--soft-blue)" stroke-width="2"/>
      </svg>
      <span>Hard Drive Cleanup</span>
    </li>
    <li class="service-item" style="left:152px; top:888px;">
      <svg class="service-icon" viewBox="0 0 24 24">
        <rect x="5" y="2" width="14" height="20" rx="1.5" fill="var(--sky)"/>
        <path d="M8 6h8M8 9h8" stroke="var(--white)" stroke-width="1.5"/>
        <circle cx="12" cy="17" r="1.5" fill="var(--white)"/>
      </svg>
      <span>Server Issues</span>
    </li>
    <li class="service-item" style="left:64px; top:1040px;">
      <svg class="service-icon" viewBox="0 0 24 24">
        <rect x="3" y="3" width="14" height="17" rx="1.5" fill="none" stroke="var(--sky)" stroke-width="2"/>
        <path d="M6 8h8M6 11h8M6 14h5" stroke="var(--soft-blue)" stroke-width="1.5"/>
        <circle cx="18" cy="18" r="4" fill="var(--sky)"/>
        <path d="M16.5 16.5l3 3M19.5 16.5l-3 3" stroke="var(--white)" stroke-width="1.2"/>
      </svg>
      <span>Program Cleanup</span>
    </li>
  </ul>

  <footer class="contact-band">Call 908-555-0142</footer>
</main>
</body>
</html>
```